Business Card Design needed for logo design project

This project is linked to http://gigs.artbazaarhub.net/task.aspx?id=417962

Our company needs a Business Card Design. Please refer to our original project in the link above for the logo and here is the content for the card-

KV&T
Gearwell Supplies & Solutions, Inc.

Doreen Whitcombe

Toll Free (800) 555-3174
Phone (936) 555-0428
Fax (936) 555-7352
4816 E. FM 2231
Willis, Texas 77594
info@kvt-grove.com
www.kvt-grove.com

```html
<!DOCTYPE html>
<html lang="en">
<head>
<meta charset="utf-8">
<title>KV&amp;T Business Card</title>
<link rel="stylesheet" href="https://fonts.googleapis.com/css2?family=Open+Sans:wght@400;600;700;800&display=swap">
<style>
  :root {
    --page-bg: #ece8e1;
    --gold-light: #f3dca0;
    --gold: #d7a64a;
    --gold-deep: #a8742a;
    --ink: #1c1c1c;
    --text: #3a3a3a;
    --card-white: #ffffff;
    --steel-light: #b9b9b9;
    --steel-dark: #5e5e5e;
  }
  * { box-sizing: border-box; margin: 0; padding: 0; }
  html, body {
    width: 1200px; height: 900px; overflow: hidden;
    background: var(--page-bg);
    font-family: "Open Sans", Arial, sans-serif;
  }
  .canvas { position: relative; width: 1200px; height: 900px; }

  .card {
    position: absolute; left: 285px; width: 630px; height: 360px;
    border-radius: 16px; overflow: hidden;
    box-shadow: 0 10px 28px rgba(0,0,0,.18);
  }

  /* back side */
  .card-back {
    top: 50px;
    background: radial-gradient(ellipse at 45% 40%, var(--gold-light) 0%, #e0bd78 45%, var(--gold-deep) 100%);
  }
  .card-back .texture {
    position: absolute; inset: 0;
    background: linear-gradient(135deg, rgba(255,255,255,.10), rgba(120,80,20,.12));
  }
  .card-back .brand-name {
    position: absolute; left: 0; right: 0; top: 140px;
    text-align: center; font-weight: 800; font-size: 72px;
    letter-spacing: 6px; color: var(--ink);
  }

  /* front side */
  .card-front { top: 450px; background: var(--card-white); }
  .front-logo { position: absolute; left: 34px; top: 24px; }
  .front-logo .brand-name {
    font-weight: 800; font-size: 58px; line-height: 1;
    letter-spacing: 4px; color: var(--gold);
  }
  .front-logo .tagline {
    margin-top: 6px; font-size: 9.5px; font-weight: 600;
    letter-spacing: .6px; text-transform: uppercase; color: var(--text);
  }
  .chain-band {
    position: absolute; left: 34px; top: 150px; width: 460px; height: 8px;
    border-radius: 4px;
    background: linear-gradient(180deg, var(--steel-light), var(--steel-dark));
  }
  .contact-list {
    position: absolute; left: 34px; top: 178px; list-style: none;
    font-size: 13px; color: var(--text);
  }
  .contact-list li { display: flex; align-items: center; gap: 8px; height: 21px; white-space: nowrap; }
  .contact-list .label { font-weight: 600; color: var(--ink); }
  .contact-list svg { width: 13px; height: 13px; fill: var(--gold); flex: none; }

  .person { position: absolute; right: 40px; top: 170px; text-align: right; }
  .person .name { font-size: 22px; font-weight: 600; color: var(--gold); white-space: nowrap; }
  .person .role { font-size: 14px; font-weight: 600; color: var(--ink); }

  .address {
    position: absolute; right: 40px; top: 248px; text-align: right;
    font-size: 13px; line-height: 1.4; color: var(--text); white-space: nowrap;
  }

  .footer-bands { position: absolute; left: 0; bottom: 0; width: 630px; height: 60px; }
  .website {
    position: absolute; right: 60px; bottom: 18px;
    font-size: 15px; font-weight: 600; letter-spacing: 3px; color: var(--ink);
  }
</style>
</head>
<body>
<main class="canvas">

  <section class="card card-back" aria-label="Card back">
    <div class="texture" role="img" aria-label="Faint repeated company name texture across the gold surface"></div>
    <div class="brand-name">KV&amp;T</div>
  </section>

  <section class="card card-front" aria-label="Card front">
    <div class="front-logo">
      <div class="brand-name">KV&amp;T</div>
      <div class="tagline">Gearwell Supplies &amp; Solutions, Inc.</div>
    </div>

    <div class="chain-band" role="img" aria-label="Steel roller chain running across the card"></div>

    <ul class="contact-list">
      <li><svg viewBox="0 0 16 16"><path d="M3 1h3l1 4-2 1c1 2 3 4 5 5l1-2 4 1v3c0 1-1 2-2 2C7 15 1 9 1 3c0-1 1-2 2-2z"/></svg><span class="label">Toll Free</span> (800) 555-3174</li>
      <li><svg viewBox="0 0 16 16"><path d="M4 0h8a1 1 0 0 1 1 1v14a1 1 0 0 1-1 1H4a1 1 0 0 1-1-1V1a1 1 0 0 1 1-1zm1 2v10h6V2z"/></svg><span class="label">Phone</span> (936) 555-0428</li>
      <li><svg viewBox="0 0 16 16"><path d="M4 0h7v4H4zM1 5h14v7h-3v4H4v-4H1zm5 7v2h4v-2z"/></svg><span class="label">Fax</span> (936) 555-7352</li>
      <li><svg viewBox="0 0 16 16"><path d="M0 3h16v10H0zm1 1 7 5 7-5z"/></svg>info@kvt-grove.com</li>
    </ul>

    <div class="person">
      <div class="name">Doreen Whitcombe</div>
      <div class="role">Director</div>
    </div>

    <div class="address">
      4816 E. FM 2231<br>
      Willis, Texas 77594
    </div>

    <svg class="footer-bands" viewBox="0 0 630 60" preserveAspectRatio="none" aria-hidden="true">
      <defs>
        <linearGradient id="goldBand" x1="0" y1="0" x2="1" y2="0">
          <stop offset="0" stop-color="#a8742a"/>
          <stop offset=".5" stop-color="#f3dca0"/>
          <stop offset="1" stop-color="#c08c3a"/>
        </linearGradient>
      </defs>
      <polygon points="0,4 300,4 300,18 0,18" fill="#1c1c1c"/>
      <polygon points="0,22 300,22 330,8 630,8 630,60 0,60" fill="url(#goldBand)"/>
    </svg>
    <div class="website">www.kvt-grove.com</div>
  </section>

</main>
</body>
</html>
```